A empresa queria:
" Pista de Tiro indoor, pessoas pagam por ano ou por visita aluguel de pista de tiro aluguel de arma venda de arma venda de munição cursos de tiro Documentação para aquisição de arma CAÇA DE JAVALI "

```html
<!DOCTYPE html>
<html lang="pt-BR">
<head>
<meta charset="utf-8">
<title>Davi Moreira – Despachante de Armas</title>
<link rel="stylesheet" href="https://fonts.googleapis.com/css2?family=Rajdhani:wght@500;700&family=Roboto:wght@400;700&display=swap">
<style>
  :root {
    --page: #e9eaec;
    --ink: #121316;
    --panel: #1b1c20;
    --panel-2: #26272c;
    --red: #d8232a;
    --red-dark: #9e151b;
    --white: #ffffff;
    --muted: #b9bbc0;
    --sun: #f39a2b;
    --sun-deep: #c4521a;
  }
  * { box-sizing: border-box; margin: 0; padding: 0; }
  html, body { width: 1200px; height: 1200px; overflow: hidden; }
  body {
    background: var(--page);
    font-family: "Roboto", Arial, sans-serif;
    display: flex; flex-direction: column; align-items: center; justify-content: center;
    gap: 48px;
  }

  /* Profile picture */
  .profile-pic {
    width: 300px; height: 300px;
    background: var(--panel);
    display: flex; flex-direction: column; align-items: center; justify-content: center;
    gap: 14px;
    box-shadow: 0 6px 18px rgba(0,0,0,.18);
  }
  .brand-dot {
    width: 120px; height: 120px; border-radius: 50%;
    background: var(--red);
  }
  .profile-name {
    font-family: "Rajdhani", sans-serif; font-weight: 700;
    font-size: 30px; letter-spacing: 2px; color: var(--white);
  }

  /* Cover */
  .cover {
    position: relative;
    width: 1100px; height: 418px;
    background: var(--panel);
    overflow: hidden;
    box-shadow: 0 6px 18px rgba(0,0,0,.18);
  }
  .cover-photo {
    position: absolute; top: 0; right: 0; width: 640px; height: 100%;
    background:
      radial-gradient(circle at 62% 58%, #ffd36b 0, var(--sun) 12%, var(--sun-deep) 34%, #3a1a10 62%, #0d0d0f 85%);
  }
  .cover-shape { position: absolute; inset: 0; }
  .brand {
    position: absolute; left: 70px; top: 70px; width: 360px;
    display: flex; flex-direction: column; align-items: center; gap: 18px;
  }
  .brand .brand-dot { width: 130px; height: 130px; }
  .brand-name {
    font-family: "Rajdhani", sans-serif; font-weight: 700;
    font-size: 46px; letter-spacing: 3px; color: var(--white); line-height: 1;
  }
  .brand-tag {
    font-family: "Rajdhani", sans-serif; font-weight: 500;
    font-size: 18px; letter-spacing: 5px; color: var(--muted);
  }
  .services {
    position: absolute; right: 0; bottom: 0; width: 640px; height: 92px;
    background: rgba(18,19,22,.92);
    border-top: 4px solid var(--red);
    display: flex; align-items: center; justify-content: space-around;
    padding: 0 16px;
  }
  .service {
    display: flex; align-items: center; gap: 10px;
    color: var(--white); font-size: 14px; font-weight: 700; line-height: 1.3;
  }
  .service svg { flex: none; }
  .service + .service { border-left: 1px solid var(--red); padding-left: 16px; }
</style>
</head>
<body>

  <div class="profile-pic">
    <div class="brand-dot"></div>
    <div class="profile-name">DAVI MOREIRA</div>
  </div>

  <section class="cover">
    <div class="cover-photo" role="img" aria-label="Atirador com rifle em silhueta contra o pôr do sol"></div>
    <svg class="cover-shape" width="1100" height="418" viewBox="0 0 1100 418" aria-hidden="true">
      <polygon points="0,0 500,0 400,418 0,418" fill="#1b1c20"/>
      <polygon points="500,0 540,0 440,418 400,418" fill="#d8232a"/>
      <polygon points="540,0 556,0 456,418 440,418" fill="#9e151b"/>
    </svg>

    <div class="brand">
      <div class="brand-dot"></div>
      <div class="brand-name">DAVI MOREIRA</div>
      <div class="brand-tag">DESPACHANTE DE ARMAS</div>
    </div>

    <div class="services">
      <div class="service">
        <svg width="22" height="26" viewBox="0 0 22 26"><rect x="2" y="2" width="18" height="22" rx="2" fill="none" stroke="#d8232a" stroke-width="2"/><path d="M6 9h10M6 13h10M6 17h6" stroke="#d8232a" stroke-width="2"/></svg>
        <span>Documentação para<br>aquisição de arma</span>
      </div>
      <div class="service">
        <svg width="22" height="26" viewBox="0 0 22 26"><rect x="7" y="8" width="8" height="16" fill="#d8232a"/><path d="M7 8 L11 1 L15 8 Z" fill="#d8232a"/></svg>
        <span>Venda de Munições<br>Aluguel &amp; Venda de Armas</span>
      </div>
      <div class="service">
        <svg width="26" height="26" viewBox="0 0 26 26"><circle cx="13" cy="13" r="10" fill="none" stroke="#d8232a" stroke-width="2"/><circle cx="13" cy="13" r="4" fill="#d8232a"/></svg>
        <span>Pista de Tiro Indoor<br>Cursos de Tiro</span>
      </div>
    </div>
  </section>

</body>
</html>
```